Business card design for engineering firm specializing in defense industry.

We need a professional business card design. Something simple but stands out. We are an engineering company specializing in composites in the defense industry.
Industry/Entity Type
Defense
Contact Information for Business Card
A simple black business card with the Varlonix yellow color is what we had in mind but open for other designs.
Colors
ffc214

```html
<!DOCTYPE html>
<html lang="en">
<head>
<meta charset="utf-8">
<title>Varlonix Business Card</title>
<link rel="stylesheet" href="https://fonts.googleapis.com/css2?family=Open+Sans:wght@400;800&display=swap">
<style>
  :root {
    --brand-yellow: #ffc214;
    --brand-amber: #f2b431;
    --ink-dark: #2f2f2f;
    --ink-deeper: #262626;
    --paper: #ffffff;
    --paper-shade: #e9e9e9;
    --text-grey: #3d3d3d;
    --stage: #1f1f1f;
  }
  * { margin: 0; padding: 0; box-sizing: border-box; }
  html, body { width: 1200px; height: 1200px; overflow: hidden; background: var(--stage); }
  body { font-family: "Open Sans", Arial, sans-serif; }

  .canvas { position: relative; width: 1200px; height: 1200px; }

  .card {
    position: absolute;
    left: 150px;
    width: 900px;
    height: 514px;
    overflow: hidden;
    background: var(--paper);
    box-shadow: 0 10px 30px rgba(0,0,0,0.45);
  }
  .card--front { top: 66px; }
  .card--back { top: 620px; }
  .card__art { position: absolute; inset: 0; width: 100%; height: 100%; }

  .wordmark {
    position: absolute;
    display: flex;
    align-items: center;
    gap: 14px;
    font-weight: 800;
    font-size: 58px;
    letter-spacing: 1px;
    color: var(--ink-deeper);
  }
  .wordmark__dot {
    width: 26px; height: 26px;
    background: var(--brand-yellow);
  }
  .card--front .wordmark { left: 50%; top: 50%; transform: translate(-50%, -60%); }

  .logo-pill {
    position: absolute;
    right: 70px;
    top: 190px;
    width: 300px;
    height: 130px;
    border-radius: 65px;
    background: var(--paper);
    display: flex;
    align-items: center;
    justify-content: center;
  }
  .logo-pill .wordmark { position: static; font-size: 46px; gap: 10px; }
  .logo-pill .wordmark__dot { width: 20px; height: 20px; }

  .contact-list {
    position: absolute;
    left: 60px;
    top: 70px;
    list-style: none;
  }
  .contact-list__item {
    display: flex;
    align-items: center;
    gap: 22px;
    height: 50px;
    margin-bottom: 22px;
    font-size: 17px;
    color: var(--text-grey);
    text-transform: uppercase;
  }
  .contact-list__icon {
    width: 50px; height: 50px;
    border-radius: 50%;
    background: var(--brand-amber);
    display: flex; align-items: center; justify-content: center;
    flex-shrink: 0;
  }
  .contact-list__icon svg { width: 28px; height: 28px; }
</style>
</head>
<body>
<main class="canvas">

  <!-- Front side -->
  <section class="card card--front" aria-label="Business card front">
    <svg class="card__art" viewBox="0 0 900 514" preserveAspectRatio="none" aria-hidden="true">
      <defs>
        <linearGradient id="paperFront" x1="0" y1="0" x2="0" y2="1">
          <stop offset="0" stop-color="#ffffff"/>
          <stop offset="1" stop-color="#e8e8e8"/>
        </linearGradient>
      </defs>
      <rect width="900" height="514" fill="url(#paperFront)"/>
      <path d="M560 0 H900 V150 C820 90 700 40 560 0Z" fill="var(--ink-dark)"/>
      <path d="M600 70 C740 90 860 160 900 230 V320 C850 240 740 150 600 70Z" fill="var(--brand-amber)"/>
      <path d="M0 250 C160 270 310 330 430 430 C290 380 150 340 0 330Z" fill="var(--brand-amber)"/>
      <path d="M360 514 C410 470 470 440 560 450 C700 466 820 476 900 478 V514Z" fill="var(--ink-dark)"/>
    </svg>
    <div class="wordmark"><span class="wordmark__dot"></span>Varlonix</div>
  </section>

  <!-- Back side -->
  <section class="card card--back" aria-label="Business card back">
    <svg class="card__art" viewBox="0 0 900 514" preserveAspectRatio="none" aria-hidden="true">
      <defs>
        <linearGradient id="paperBack" x1="0" y1="0" x2="0" y2="1">
          <stop offset="0" stop-color="#ffffff"/>
          <stop offset="1" stop-color="#e6e6e6"/>
        </linearGradient>
      </defs>
      <rect width="900" height="514" fill="url(#paperBack)"/>
      <path d="M560 0 H900 V514 H430 C480 430 505 330 525 250 C545 150 552 70 560 0Z" fill="var(--ink-dark)"/>
      <polygon points="560,0 900,0 720,260" fill="#ffffff" opacity="0.04"/>
      <polygon points="480,400 900,280 900,514 620,514" fill="#000000" opacity="0.12"/>
      <polygon points="640,120 900,60 900,300" fill="#ffffff" opacity="0.03"/>
      <path d="M330 514 C400 440 460 360 500 300 L514 318 C490 400 450 470 412 514Z" fill="var(--brand-amber)"/>
      <path d="M412 514 C450 470 490 400 514 318 L520 300 C505 380 470 460 430 514Z" fill="#ffffff"/>
    </svg>

    <ul class="contact-list">
      <li class="contact-list__item">
        <span class="contact-list__icon">
          <svg viewBox="0 0 24 24" fill="none" stroke="#fff" stroke-width="2" stroke-linejoin="round"><path d="M3 11 L12 4 L21 11"/><path d="M6 9 V20 H18 V9"/></svg>
        </span>
        Your adress goes here
      </li>
      <li class="contact-list__item">
        <span class="contact-list__icon">
          <svg viewBox="0 0 24 24" fill="none" stroke="#fff" stroke-width="2" stroke-linejoin="round"><rect x="3" y="6" width="18" height="12"/><path d="M3 6 L12 13 L21 6"/></svg>
        </span>
        yourweb@email.com
      </li>
      <li class="contact-list__item">
        <span class="contact-list__icon">
          <svg viewBox="0 0 24 24" fill="none" stroke="#fff" stroke-width="2" stroke-linejoin="round"><path d="M8 3 C5 4 4 7 5 10 C7 15 10 18 14 20 C17 21 20 20 21 17 L17 14 L14 16 C11 14 10 13 8 10 L10 7Z"/></svg>
        </span>
        123 - 456789
      </li>
      <li class="contact-list__item">
        <span class="contact-list__icon">
          <svg viewBox="0 0 24 24" fill="none" stroke="#fff" stroke-width="2"><circle cx="12" cy="12" r="9"/><ellipse cx="12" cy="12" rx="4" ry="9"/><path d="M3 12 H21 M5 7 H19 M5 17 H19"/></svg>
        </span>
        website.com
      </li>
    </ul>

    <div class="logo-pill">
      <div class="wordmark"><span class="wordmark__dot"></span>Varlonix</div>
    </div>
  </section>

</main>
</body>
</html>
```